Wine label design for my wife. Wine called "The Mirabel"

I need a wine label face lift of one of my premium wines in my collection. My wine sells in Harbor Lark's all over the States. My current label is called The Mirabel (my wife's name) and the illustration of her eyes is done by a well know artist from South Africa. I do not have to use this illustration and therefor I attached several pictures of her and her eyes, even when she was a little girl. The wine's also made in South Africa. This is a premium wine that we only sell 2000 bottles per year. The wine sells at 60 usd per bottle, The current label is too white. I also think her eyes should look more at the person buying it, than away from them.

Target Market(s)

Top end wine buyers

Font styles to use
Decorative
Script

Requirements
Must have
• 'The Mirabel' must be on the label
An illustration must be on the label
Basically all the info that's on the current label must be on by law. As per Sample
Nice to have
• Maybe some ideas of her whole face?
Should not have
• any gold colour

```html
<!DOCTYPE html>
<html lang="en">
<head>
<meta charset="utf-8">
<title>The Mirabel – Sauvignon Blanc Label</title>
<link href="https://fonts.googleapis.com/css2?family=Pinyon+Script&family=EB+Garamond:wght@400&display=swap" rel="stylesheet">
<style>
  :root {
    --backdrop: #d7d7d7;
    --label-black: #1b1b1d;
    --frame-line: #5a5a5c;
    --ink-white: #f4f4f4;
    --ink-soft: #bdbdbd;
    --portrait-light: #d9d3c9;
    --portrait-mid: #b9b1a5;
    --portrait-dark: #8f877c;
  }
  * { margin: 0; padding: 0; box-sizing: border-box; }
  html, body {
    width: 1200px;
    height: 960px;
    overflow: hidden;
    background: var(--backdrop);
  }
  .canvas {
    position: relative;
    width: 1200px;
    height: 960px;
  }
  .wine-label {
    position: absolute;
    left: 286px;
    top: 50px;
    width: 629px;
    height: 860px;
    background: var(--label-black);
    color: var(--ink-white);
    text-align: center;
    overflow: hidden;
  }
  .label-frame {
    position: absolute;
    inset: 12px;
    border: 1px solid var(--frame-line);
    pointer-events: none;
  }
  .wine-name {
    position: absolute;
    top: 0;
    left: 24px;
    right: 24px;
    font-family: "Pinyon Script", cursive;
    font-size: 112px;
    line-height: 130px;
    font-weight: 400;
    white-space: nowrap;
  }
  .varietal {
    position: absolute;
    top: 160px;
    left: 0;
    right: 0;
    font-family: "EB Garamond", serif;
    font-size: 44px;
    line-height: 60px;
    letter-spacing: 1px;
    white-space: nowrap;
  }
  .portrait {
    position: absolute;
    top: 317px;
    left: 82px;
    width: 464px;
    height: 166px;
    background: linear-gradient(180deg, var(--portrait-dark) 0%, var(--portrait-light) 35%, var(--portrait-mid) 100%);
  }
  .producer {
    position: absolute;
    top: 668px;
    left: 44px;
    right: 44px;
    display: flex;
    align-items: center;
    gap: 22px;
    font-family: "EB Garamond", serif;
    font-size: 40px;
    line-height: 50px;
    letter-spacing: 1px;
    white-space: nowrap;
  }
  .producer .rule {
    flex: 1;
    height: 2px;
    background: var(--ink-white);
  }
  .origin {
    position: absolute;
    top: 781px;
    left: 0;
    right: 0;
    font-family: "EB Garamond", serif;
    font-size: 20px;
    line-height: 33px;
    letter-spacing: 1px;
    color: var(--ink-soft);
  }
</style>
</head>
<body>
  <main class="canvas">
    <section class="wine-label">
      <div class="label-frame"></div>
      <h1 class="wine-name">The Mirabel</h1>
      <p class="varietal">SAUVIGNON BLANC 2017</p>
      <div class="portrait" role="img" aria-label="Illustration of Mirabel's eyes looking out at the viewer"></div>
      <p class="producer"><span class="rule"></span><span>DANIEL MARSH WINE</span><span class="rule"></span></p>
      <p class="origin">MADE IN<br>SOUTH AFRICA</p>
    </section>
  </main>
</body>
</html>
```